Business Cards for our company

Hi there,

we have successfully designed a logo with ArtFlock and would like now to design our business cards. We would like to keep the colours and the look-and-feel of the logo. Please send in variations with two or three colours and one or two sides. I promise to respond to every single submission.

Many thanks and happy new year.

All the best,
Wilfried

Target Market(s)

B2B

Industry/Entity Type

Trade

Contact Information for Business Card

We have successfully designed a logo with ArtFlock and would like now to design our business cards. We would like to keep the colours and the look-and-feel of the logo. Please send in variations with two or three colours and one or two sides. I promise to respond to every single submission.

Font styles to use
Serif
Sans Serif
Script

Requirements
Must have
• These information should be on the business card, grouped as you suggest, and we think using small pictograms for mobile, email, etc is pretty helpful:
• Wilfried Tammler (first and second name)
• Geschäftsführer/ Managing Director (title)
• KoR Warenkontor GmbH (company name and legal form)
• Ostheimer Str. 18/3 (street and house number)
• 70000 Musterfeld (zip code and town)
• +491709384562 (mobile)
• +4971569027341 (work)
• w.tammler@kor-warenkontor.example (email)
• www.kor-warenkontor.example (web)
Nice to have
• Spectacular and interesting layout and design. You look at it and think, wow, that's not the normal stuff.
• We think of ourselves as bridge-builders between businesses (international producers on the one hand, and retail chains on the other hand) and we translate, organise and manage projects where both partners are involved, but it's difficult for them to cooperate due to language barriers and different working cultures.
• This is why we have the n between the B's shaped as a bridge, and the green arc supports this idea. Maybe you could play with this idea...
Should not have
• the standard layout that everybody has

```html
<!DOCTYPE html>
<html lang="de">
<head>
<meta charset="utf-8">
<title>KoR Warenkontor – Visitenkarten</title>
<link rel="stylesheet" href="https://fonts.googleapis.com/css2?family=Open+Sans:wght@400;600;700&display=swap">
<style>
  :root {
    --bg: #d9d1c5;
    --card-black: #0b0b0b;
    --card-white: #ffffff;
    --brand-green: #2aac4a;
    --text-light: #f2f2f2;
    --font-main: "Open Sans", Arial, sans-serif;
  }
  * { box-sizing: border-box; margin: 0; padding: 0; }
  html, body { width: 1200px; height: 900px; overflow: hidden; }
  body { background: var(--bg); font-family: var(--font-main); position: relative; }

  .card {
    position: absolute;
    width: 600px;
    height: 343px;
    border-radius: 4px;
    overflow: hidden;
    box-shadow: 0 14px 30px rgba(0,0,0,.28);
  }
  .card-front { left: 70px; top: 100px; background: var(--card-white); }
  .card-back  { left: 530px; top: 480px; background: var(--card-black); }

  .front-shapes { position: absolute; inset: 0; }

  .brand-name {
    font-family: var(--font-main);
    font-weight: 700;
    letter-spacing: .5px;
    line-height: 1;
    white-space: nowrap;
  }
  .card-front .brand-name {
    position: absolute;
    right: 40px;
    top: 58px;
    font-size: 34px;
    color: var(--card-black);
  }
  .card-back .brand-name {
    position: absolute;
    left: 0; right: 0;
    top: 150px;
    text-align: center;
    font-size: 44px;
    color: var(--card-white);
  }

  .contact {
    position: absolute;
    left: 34px;
    top: 128px;
    color: var(--text-light);
    font-size: 12.5px;
    line-height: 1.45;
  }
  .contact-name { font-size: 19px; font-weight: 700; color: #fff; line-height: 1.2; }
  .contact-title { color: var(--brand-green); font-size: 12.5px; margin-bottom: 8px; }
  .contact-address { margin-bottom: 6px; }
  .contact-list { list-style: none; }
  .contact-list li { display: flex; align-items: center; gap: 8px; }
  .contact-list svg { width: 11px; height: 11px; flex: none; fill: var(--brand-green); }
</style>
</head>
<body>

<section class="card card-front">
  <svg class="front-shapes" viewBox="0 0 600 343" preserveAspectRatio="none" aria-hidden="true">
    <path d="M0,52 Q330,62 620,330 L620,343 L0,343 Z" fill="var(--brand-green)"/>
    <path d="M0,66 Q328,76 610,336 L610,343 L0,343 Z" fill="var(--card-white)"/>
    <path d="M0,76 Q322,86 600,343 L0,343 Z" fill="var(--card-black)"/>
  </svg>

  <div class="brand-name">KoR Warenkontor</div>

  <div class="contact">
    <p class="contact-name">Wilfried Tammler</p>
    <p class="contact-title">Geschäftsführer/ Managing Director</p>
    <p class="contact-address">Ostheimer Str. 18/3<br>70000 Musterfeld<br>Deutschland</p>
    <ul class="contact-list">
      <li><svg viewBox="0 0 12 12"><rect x="3" y="0" width="6" height="12" rx="1.2"/></svg>+49 170 9990456</li>
      <li><svg viewBox="0 0 12 12"><path d="M2 1 L5 1 L6 4 L4.5 5.2 Q6 8 7 7.5 L8 6 L11 7 L11 10 Q6 12 2 6 Q0.5 3 2 1 Z"/></svg>+49 7990 9027341 (work)</li>
      <li><svg viewBox="0 0 12 12"><rect x="1" y="4" width="10" height="7" rx="1"/><rect x="3" y="1" width="6" height="4"/></svg>+49 7990 9027342</li>
      <li><svg viewBox="0 0 12 12"><path d="M0 2 H12 V10 H0 Z M0 2 L6 7 L12 2" /></svg>w.tammler@kor-warenkontor.example</li>
      <li><svg viewBox="0 0 12 12"><circle cx="6" cy="6" r="6"/></svg>www.kor-warenkontor.example</li>
    </ul>
  </div>
</section>

<section class="card card-back">
  <div class="brand-name">KoR Warenkontor</div>
</section>

</body>
</html>
```